Amber Orchard (instructional dating book)

Title: Amber Orchard
Subtitle: Where to plant tulips along a crooked brick path
Author: R.K. Tolvane
I'm seeking the title to be central with the subtitle underneath and the author slightly lower and to the left. Perhaps a border or two around the font. I thought the background could look aged (off color and old textured paper) and the background slightly punched into the texture like a typewriter has been used. I imagine it something like an old Pemberworth playbook or 1940s morse code manual. Many thanks!

Target Market(s)

18 to 45 year old single people

Industry/Entity Type

Dating

Font styles to use
Serif

Requirements
Must have
• Text with border or two
Nice to have
• Traditional feel. The book is instructional.
Should not have
• Too much color or flair

```html
<!DOCTYPE html>
<html lang="en">
<head>
<meta charset="utf-8">
<title>Amber Orchard — R.K. Tolvane</title>
<link rel="stylesheet" href="https://fonts.googleapis.com/css2?family=Cinzel:wght@400;500;600&display=swap">
<style>
  :root {
    --page-bg: #ffffff;
    --paper-light: #f1e4c6;
    --paper-mid: #e6d3ac;
    --paper-edge: #c9ab78;
    --paper-stain: #b8955c;
    --ink: #3a2a22;
    --wood-light: #ead7b0;
    --wood-mid: #d6b783;
    --wood-dark: #a27a48;
  }
  * { margin: 0; padding: 0; box-sizing: border-box; }
  html, body {
    width: 1200px;
    height: 1135px;
    overflow: hidden;
    background: var(--page-bg);
  }
  .canvas {
    position: relative;
    width: 1200px;
    height: 1135px;
    display: flex;
    align-items: center;
    justify-content: center;
  }
  .book-cover {
    position: relative;
    width: 690px;
    height: 1105px;
    overflow: hidden;
    background:
      radial-gradient(ellipse at 50% 38%, var(--paper-light) 0%, var(--paper-mid) 60%, var(--paper-edge) 100%);
    color: var(--ink);
    font-family: "Cinzel", "Times New Roman", serif;
    text-align: center;
    text-transform: uppercase;
  }
  .paper-texture {
    position: absolute;
    inset: 0;
    width: 100%;
    height: 100%;
    pointer-events: none;
  }
  .cover-frame {
    position: absolute;
    top: 28px;
    left: 28px;
    right: 28px;
    height: 612px;
    border: 7px double var(--ink);
    opacity: 0.85;
  }
  .cover-frame::after {
    content: "";
    position: absolute;
    inset: 8px;
    border: 1px solid var(--ink);
    opacity: 0.6;
  }
  .cover-text {
    position: absolute;
    top: 28px;
    left: 28px;
    right: 28px;
    height: 612px;
  }
  .ink {
    text-shadow: 0 1px 0 rgba(255, 248, 230, 0.55), 0 -1px 1px rgba(40, 25, 15, 0.25);
  }
  .cover-title {
    position: absolute;
    top: 48px;
    left: 0;
    right: 0;
    font-weight: 600;
    font-size: 80px;
    line-height: 1.22;
    letter-spacing: 0.2em;
    padding-left: 0.2em;
  }
  .cover-title span { display: block; }
  .cover-subtitle {
    position: absolute;
    top: 292px;
    left: 0;
    right: 0;
    font-size: 31px;
    line-height: 1.3;
    font-weight: 500;
  }
  .cover-subtitle span { display: block; }
  .cover-author {
    position: absolute;
    top: 520px;
    left: 0;
    right: 0;
    font-size: 36px;
    font-weight: 500;
    letter-spacing: 0.03em;
  }
  .cover-photo {
    position: absolute;
    left: 0;
    right: 0;
    bottom: 0;
    height: 440px;
    background:
      linear-gradient(to bottom, rgba(230,211,172,1) 0%, rgba(230,211,172,0) 20%),
      linear-gradient(to bottom, var(--wood-light) 0%, var(--wood-mid) 55%, var(--wood-dark) 100%);
  }
</style>
</head>
<body>
  <main class="canvas">
    <article class="book-cover">
      <svg class="paper-texture" viewBox="0 0 690 1105" preserveAspectRatio="none" aria-hidden="true">
        <defs>
          <filter id="paper-grain" x="0" y="0" width="100%" height="100%">
            <feTurbulence type="fractalNoise" baseFrequency="0.9" numOctaves="3" seed="4" result="grain"/>
            <feColorMatrix in="grain" type="matrix"
              values="0 0 0 0 0.45  0 0 0 0 0.33  0 0 0 0 0.18  0 0 0 0.55 -0.12"/>
          </filter>
          <filter id="paper-mottle" x="0" y="0" width="100%" height="100%">
            <feTurbulence type="fractalNoise" baseFrequency="0.012 0.018" numOctaves="4" seed="11" result="mottle"/>
            <feColorMatrix in="mottle" type="matrix"
              values="0 0 0 0 0.62  0 0 0 0 0.47  0 0 0 0 0.25  0 0 0 1.1 -0.45"/>
          </filter>
          <radialGradient id="paper-vignette" cx="50%" cy="35%" r="75%">
            <stop offset="60%" stop-color="#b8955c" stop-opacity="0"/>
            <stop offset="100%" stop-color="#b8955c" stop-opacity="0.45"/>
          </radialGradient>
        </defs>
        <rect width="690" height="700" filter="url(#paper-mottle)" opacity="0.75"/>
        <rect width="690" height="700" filter="url(#paper-grain)" opacity="0.6"/>
        <rect width="690" height="700" fill="url(#paper-vignette)"/>
      </svg>

      <div class="cover-frame" aria-hidden="true"></div>

      <div class="cover-text">
        <h1 class="cover-title ink"><span>Amber</span><span>Orchard</span></h1>
        <p class="cover-subtitle ink">
          <span>Where to plant</span>
          <span>tulips along a</span>
          <span>crooked brick</span>
          <span>path</span>
        </p>
        <p class="cover-author ink">R.K. Tolvane</p>
      </div>

      <div class="cover-photo" role="img" aria-label="Close-up photograph of many wooden letter dice spread across a surface, fading into the distance"></div>
    </article>
  </main>
</body>
</html>
```